Logo and bussiness card stationary design

I want bussiness cards ann stationary that would mactch with the design of my website:

drmarcelvantroy.com.au

Logo Text

Dr Marcel Vantroy

```html
<!DOCTYPE html>
<html lang="en">
<head>
<meta charset="utf-8">
<title>Dr Marcel Vantroy – Appointment &amp; Business Card</title>
<link rel="stylesheet" href="https://fonts.googleapis.com/css2?family=Nunito:wght@600;700;800&display=swap">
<style>
  :root {
    --teal: #4bb2c4;
    --teal-soft: #9ccfdb;
    --teal-deep: #3a97a8;
    --teal-faint: #bddde6;
    --mint: #93d3c8;
    --orange: #f08a24;
    --ink: #1d2f47;
    --white: #ffffff;
    --card-edge: #9aa7ad;
    --page-top: #ffffff;
    --page-bottom: #9dcedb;
  }
  * { box-sizing: border-box; margin: 0; padding: 0; }
  html, body { width: 1200px; height: 1000px; overflow: hidden; }
  body {
    position: relative;
    background: linear-gradient(180deg, var(--page-top) 0%, #d6eaf0 45%, var(--page-bottom) 100%);
    font-family: "Nunito", Arial, sans-serif;
    color: var(--ink);
  }
  .card {
    position: absolute;
    left: 245px;
    width: 711px;
    height: 407px;
    border: 1px solid var(--card-edge);
    overflow: hidden;
  }
  .card--appointment { top: 26px; background: var(--teal); }
  .card--contact { top: 522px; background: var(--white); }

  .card__art { position: absolute; inset: 0; }

  .appointment__title {
    position: absolute; top: 18px; left: 0; right: 0;
    text-align: center; color: var(--white);
    font-size: 27px; font-weight: 800; letter-spacing: 0.6px;
  }
  .day {
    position: absolute; width: 50px; height: 50px; border-radius: 50%;
    background: var(--white); color: var(--orange);
    font-size: 14px; font-weight: 800;
    display: flex; align-items: center; justify-content: center;
  }
  .field-label {
    position: absolute; font-size: 14px; font-weight: 800; color: var(--ink);
  }
  .brand-seal {
    position: absolute; left: 493px; top: 133px;
    width: 152px; height: 152px; border-radius: 50%;
    background: var(--mint); border: 6px solid #e2e6e7;
    display: flex; align-items: center; justify-content: center;
    text-align: center; color: var(--white);
    font-size: 17px; font-weight: 800; line-height: 1.2; padding: 0 14px;
  }

  .contact__name {
    position: absolute; right: 45px; top: 70px;
    color: var(--teal); font-size: 30px; font-weight: 800; letter-spacing: 0.6px;
  }
  .contact__band {
    position: absolute; left: 0; right: 0; top: 159px; height: 85px;
    background: var(--teal);
    border-top: 2px solid var(--orange); border-bottom: 2px solid var(--orange);
    display: flex; align-items: center; justify-content: center;
    color: var(--white); font-size: 46px; font-weight: 600; letter-spacing: 1px;
  }
  .contact__offices {
    position: absolute; top: 275px; left: 0; right: 0;
    display: flex; font-size: 21px; font-weight: 700; line-height: 27px;
  }
  .office { font-style: normal; }
  .office--sydney {
    flex: 0 0 370px; text-align: right; padding-right: 18px;
    border-right: 2px solid var(--ink);
  }
  .office--melbourne { flex: 0 0 300px; padding-left: 18px; }
  .office__city { font-size: 22px; }
</style>
</head>
<body>

<section class="card card--appointment" aria-label="Appointment card">
  <svg class="card__art" width="711" height="407" viewBox="0 0 711 407">
    <defs>
      <linearGradient id="toothFillDark" x1="0" y1="0" x2="0" y2="1">
        <stop offset="0" stop-color="#a3d3de"/>
        <stop offset="1" stop-color="#8ccbd8"/>
      </linearGradient>
      <radialGradient id="sparkleFillDark">
        <stop offset="0" stop-color="var(--teal-deep)"/>
        <stop offset="1" stop-color="var(--teal-deep)" stop-opacity="0"/>
      </radialGradient>
    </defs>
    <rect role="img" aria-label="Large faint tooth illustration" x="0" y="10" width="285" height="380" rx="60" fill="url(#toothFillDark)" opacity="0.85"/>
    <rect role="img" aria-label="Sparkle ornament" x="140" y="75" width="66" height="66" rx="33" fill="url(#sparkleFillDark)"/>
    <circle cx="348" cy="230" r="161" fill="var(--white)"/>
    <line x1="243" y1="165" x2="453" y2="165" stroke="var(--orange)" stroke-width="2"/>
    <line x1="251" y1="242" x2="460" y2="242" stroke="var(--orange)" stroke-width="2"/>
  </svg>

  <h1 class="appointment__title">YOUR NEXT APPOINTMENT IS ON:</h1>

  <span class="day" style="left:182px;top:65px">MON</span>
  <span class="day" style="left:140px;top:129px">TUE</span>
  <span class="day" style="left:128px;top:198px">WED</span>
  <span class="day" style="left:139px;top:262px">THU</span>
  <span class="day" style="left:175px;top:327px">FRI</span>

  <span class="field-label" style="left:215px;top:227px">AT</span>
  <span class="field-label" style="left:391px;top:218px">AM</span>
  <span class="field-label" style="left:447px;top:218px">PM</span>

  <div class="brand-seal">Dr Marcel Vantroy</div>
</section>

<section class="card card--contact" aria-label="Business card">
  <svg class="card__art" width="711" height="407" viewBox="0 0 711 407">
    <defs>
      <linearGradient id="toothFillLight" x1="0" y1="0" x2="0" y2="1">
        <stop offset="0" stop-color="var(--teal-faint)"/>
        <stop offset="1" stop-color="#cfe7ee"/>
      </linearGradient>
      <radialGradient id="sparkleFillLight">
        <stop offset="0" stop-color="var(--teal-faint)"/>
        <stop offset="1" stop-color="var(--teal-faint)" stop-opacity="0"/>
      </radialGradient>
    </defs>
    <rect role="img" aria-label="Large faint tooth illustration" x="22" y="120" width="262" height="275" rx="50" fill="url(#toothFillLight)"/>
    <rect role="img" aria-label="Sparkle ornament" x="190" y="0" width="110" height="95" rx="47" fill="url(#sparkleFillLight)"/>
    <rect role="img" aria-label="Small sparkle ornament" x="305" y="8" width="60" height="52" rx="26" fill="url(#sparkleFillLight)"/>
  </svg>

  <h2 class="contact__name">DR. MARCEL VANTROY</h2>

  <div class="contact__band">1 300 548 266</div>

  <div class="contact__offices">
    <address class="office office--sydney">
      <div class="office__city">SYDNEY</div>
      Suite 6 Level 9, 240<br>Harbourview Street<br>Sydney NSW 2000
    </address>
    <address class="office office--melbourne">
      <div class="office__city">MELBOURNE</div>
      Level 5, 318<br>Lanewood Street<br>Melbourne VIC 3000
    </address>
  </div>
</section>

</body>
</html>
```